Word Cloud Graphic Wallpaper design

The following sentences need to be put together in an ai file of the size : 70" wide and 108" high . This will be used as a wall paper. Inspirational image is attached. (We have also attached a rough idea showing you the wall it would go one- DO NOT REPLICATE THE LAYOUT OF THE SENTENCES-This only shows you how we will be using your file)

Sentences are:

Dentistry is not Expensive Neglect is!
Smiles are free but they are worth alot.
Don't Forget to Floss!
Put on your best SMILE everyday!
Be the reason someone smiles today.
Let your SMILE CHANGE THE WORLD, don't let the world change your smile.
Make your smile your signature accessory!

These should be in different fonts (clean modern fonts only please- no cursive or busy fonts - Helvetica Neue, Arial and fonts such as those are preferred) and sizes and should be easily legible (minimum font height 4"). Repetitions are ok if needed to fill space.

Font styles to use
Sans Serif

Requirements
Must have
• hese should be in different fonts (clean modern fonts only please- no cursive or busy fonts - Helvetica Neue, Arial and fonts such as those) and sizes and should be easily legible (minimum font height 4"). Repetitions are ok if needed to fill space.
Should not have
• Cursive, busy, fonts.

```html
<!DOCTYPE html>
<html lang="en">
<head>
<meta charset="utf-8">
<title>Smile Word Cloud Wallpaper</title>
<link rel="stylesheet" href="https://fonts.googleapis.com/css2?family=Archivo+Black&family=Arimo:wght@400;700&family=Audiowide&family=Open+Sans:wght@300;400&family=Oswald:wght@300;600;700&family=Lato:wght@100&display=swap">
<style>
  :root {
    --backdrop: #c4cfcf;
    --sheet: #ffffff;
    --sheet-shadow: rgba(0,0,0,0.28);
    --azure: #0a84ff;
    --cyan: #00f2f2;
    --red: #f50d0d;
    --ink: #000000;
    --teal: #1a8c8c;
    --royal: #0a0ae0;
    --lime: #22ee22;
    --tan: #c9a45c;
    --magenta: #ff08f0;
    --olive: #7b7010;
  }
  html, body {
    margin: 0;
    padding: 0;
    width: 1200px;
    height: 1200px;
    overflow: hidden;
    background: var(--backdrop);
  }
  .wallpaper { display: block; width: 1200px; height: 1200px; }
  .sheet { fill: var(--sheet); }
  .sheet-shadow { fill: var(--sheet-shadow); }
  .heavy { font-family: "Archivo Black", "Arial Black", sans-serif; }
  .grotesk { font-family: "Arimo", Arial, sans-serif; font-weight: 700; }
  .grotesk-regular { font-family: "Arimo", Arial, sans-serif; font-weight: 400; }
  .humanist { font-family: "Open Sans", Arial, sans-serif; font-weight: 400; }
  .humanist-light { font-family: "Open Sans", Arial, sans-serif; font-weight: 300; }
  .condensed { font-family: "Oswald", "Arial Narrow", sans-serif; font-weight: 700; }
  .condensed-semi { font-family: "Oswald", "Arial Narrow", sans-serif; font-weight: 600; }
  .condensed-light { font-family: "Oswald", "Arial Narrow", sans-serif; font-weight: 300; }
  .hairline { font-family: "Lato", Arial, sans-serif; font-weight: 100; }
  .techno { font-family: "Audiowide", Arial, sans-serif; }
  .azure { fill: var(--azure); }
  .cyan { fill: var(--cyan); }
  .red { fill: var(--red); }
  .ink { fill: var(--ink); }
  .teal { fill: var(--teal); }
  .royal { fill: var(--royal); }
  .lime { fill: var(--lime); }
  .tan { fill: var(--tan); }
  .magenta { fill: var(--magenta); }
  .olive { fill: var(--olive); }
</style>
</head>
<body>
<svg class="wallpaper" viewBox="0 0 1500 1500" xmlns="http://www.w3.org/2000/svg" role="img" aria-label="Dental smile word cloud wallpaper">
  <rect class="sheet-shadow" x="283" y="26" width="946" height="1460"/>
  <rect class="sheet" x="277" y="20" width="946" height="1460"/>

  <g class="line-dentistry">
    <text class="heavy azure" x="290" y="115" font-size="112" textLength="575" lengthAdjust="spacingAndGlyphs">Dentistry</text>
    <text class="grotesk azure" x="895" y="122" font-size="86" textLength="315" lengthAdjust="spacingAndGlyphs">IS NOT</text>
    <text class="grotesk cyan" x="288" y="208" font-size="72" textLength="417" lengthAdjust="spacingAndGlyphs">EXPENSIVE</text>
    <text class="grotesk-regular cyan" x="733" y="208" font-size="72" textLength="424" lengthAdjust="spacingAndGlyphs">NEGLECT is</text>
    <text class="grotesk azure" x="1150" y="248" font-size="150" transform="skewX(-18) translate(80 0)">!</text>
  </g>

  <g class="line-smiles-free">
    <text class="heavy red" x="290" y="292" font-size="96" textLength="410" lengthAdjust="spacingAndGlyphs">Smiles</text>
    <text class="humanist red" x="710" y="292" font-size="92" textLength="140" lengthAdjust="spacingAndGlyphs">are</text>
    <text class="heavy red" x="868" y="355" font-size="165" textLength="322" lengthAdjust="spacingAndGlyphs">Free</text>
    <text class="humanist red" x="290" y="375" font-size="98" textLength="560" lengthAdjust="spacingAndGlyphs">but they are</text>
    <text class="heavy red" x="563" y="452" font-size="96" textLength="647" lengthAdjust="spacingAndGlyphs">worth alot.</text>
  </g>

  <g class="line-floss">
    <text class="condensed ink" x="290" y="500" font-size="112" textLength="250" lengthAdjust="spacingAndGlyphs">DON'T</text>
    <text class="condensed ink" x="290" y="588" font-size="105" textLength="265" lengthAdjust="spacingAndGlyphs">Forget</text>
    <text class="hairline teal" x="345" y="658" font-size="78" textLength="93" lengthAdjust="spacingAndGlyphs">To</text>
    <text class="condensed ink" x="290" y="725" font-size="108" textLength="240" lengthAdjust="spacingAndGlyphs">Floss!</text>
  </g>

  <g class="line-best-smile">
    <text class="grotesk royal" transform="translate(628 735) rotate(-90)" font-size="90" textLength="280" lengthAdjust="spacingAndGlyphs">Put on</text>
    <text class="grotesk royal" transform="translate(708 655) rotate(-90)" font-size="82" textLength="195" lengthAdjust="spacingAndGlyphs">your</text>
    <text class="heavy royal" x="737" y="535" font-size="96" textLength="220" lengthAdjust="spacingAndGlyphs">best</text>
    <text class="heavy royal" x="748" y="657" font-size="142" textLength="460" lengthAdjust="spacingAndGlyphs">SMILE</text>
    <text class="heavy royal" x="658" y="735" font-size="100" textLength="502" lengthAdjust="spacingAndGlyphs">everyday!</text>
  </g>

  <g class="line-reason">
    <text class="techno lime" x="288" y="815" font-size="74" textLength="922" lengthAdjust="spacingAndGlyphs">BE THE REASON</text>
    <text class="techno tan" x="752" y="880" font-size="64" textLength="458" lengthAdjust="spacingAndGlyphs">SOMEONE</text>
    <text class="techno tan" x="290" y="978" font-size="124" textLength="610" lengthAdjust="spacingAndGlyphs">SMILES</text>
    <text class="condensed-light tan" x="918" y="978" font-size="92" textLength="292" lengthAdjust="spacingAndGlyphs">TODAY.</text>
  </g>

  <g class="line-change">
    <text class="heavy magenta" x="290" y="1065" font-size="98" textLength="922" lengthAdjust="spacingAndGlyphs">Let your SMILES</text>
    <text class="condensed magenta" x="293" y="1148" font-size="72" textLength="632" lengthAdjust="spacingAndGlyphs">CHANGE THE WORLD,</text>
    <text class="condensed magenta" x="293" y="1218" font-size="72" textLength="642" lengthAdjust="spacingAndGlyphs">DON'T LET THE WORLD</text>
    <text class="condensed magenta" x="940" y="1215" font-size="108" textLength="267" lengthAdjust="spacingAndGlyphs">CHANGE</text>
    <text class="grotesk magenta" x="640" y="1285" font-size="88" textLength="572" lengthAdjust="spacingAndGlyphs">YOUR SMILE.</text>
  </g>

  <g class="line-signature">
    <text class="grotesk ink" x="293" y="1345" font-size="152" textLength="357" lengthAdjust="spacingAndGlyphs">Make</text>
    <text class="heavy ink" x="668" y="1350" font-size="72" textLength="542" lengthAdjust="spacingAndGlyphs">YOUR SMILE</text>
    <text class="humanist-light ink" x="297" y="1408" font-size="92" textLength="163" lengthAdjust="spacingAndGlyphs">your</text>
    <text class="condensed-semi olive" x="460" y="1462" font-size="124" textLength="485" lengthAdjust="spacingAndGlyphs">SIGNATURE</text>
    <text class="condensed ink" x="955" y="1408" font-size="70" textLength="235" lengthAdjust="spacingAndGlyphs">access</text>
    <text class="condensed ink" x="1048" y="1464" font-size="62" textLength="162" lengthAdjust="spacingAndGlyphs">ORY!</text>
  </g>
</svg>
</body>
</html>
```